Website Home Page for Women's Health Medical Office

Redesign existing homepage for website using existing logo. Current website location is www.larkfieldwomenscare.com. Please give it a modern, streamlined, playful feel.

Please give it a feminine feel and make it bright and cheerful using logo colors.

Target Market(s)

Women between the ages of 25-45

Industry/Entity Type

Medical Office

Coding

Coded - Design and coding required

Number of Pages Required

1 page

Font styles to use
Sans Serif
Other font styles liked:
• SEGOI UI script for text and GIL SANS for bold (or their equivilent)

Colors
E54698
E96AAD
F1A4CE
F9D9EA
FCEFF6

Requirements
Must have
• Existing logo. Logo Colors. Feminine, cheerful, simple design. all relevant contact information
Nice to have
• clean lines and streamlined look
Should not have
• Cluttered

```html
<!DOCTYPE html>
<html lang="en">
<head>
<meta charset="utf-8">
<title>Larkfield Women's Care – Home</title>
<link rel="stylesheet" href="https://fonts.googleapis.com/css2?family=Montserrat:wght@400;500;600;700&family=Open+Sans:wght@400;600&display=swap">
<style>
:root{
  --pink:#E54698;
  --pink-mid:#E96AAD;
  --pink-soft:#F1A4CE;
  --pink-pale:#F9D9EA;
  --pink-mist:#FCEFF6;
  --ink:#2b2b2b;
  --text:#555;
  --grey-bg:#efedee;
  --white:#fff;
}
*{box-sizing:border-box;margin:0;padding:0}
html,body{width:1200px;height:4003px;overflow:hidden}
body{position:relative;background:var(--white);font-family:"Open Sans",sans-serif;color:var(--text)}
.abs{position:absolute}
h1,h2,h3,h4{font-family:"Montserrat",sans-serif;font-weight:500}
.btn{display:inline-block;border-radius:30px;font-family:"Montserrat",sans-serif;font-weight:500;font-size:13px;text-transform:uppercase;text-align:center}
.btn-white{background:var(--white);color:var(--pink)}
.btn-pink{background:var(--pink);color:var(--white)}
.btn-outline{border:2px solid var(--pink);color:var(--pink);background:var(--white)}

/* top bar */
.topbar{left:0;top:0;width:1200px;height:36px;background:var(--pink);color:var(--white);font-family:"Montserrat",sans-serif;font-size:11px;font-weight:600}
.topbar .follow{left:113px;top:11px}
.social-dots{display:flex;gap:7px}
.social-dots span{width:26px;height:26px;border-radius:50%;background:var(--white);display:block}
.topbar .social-dots{position:absolute;left:200px;top:5px}
.topbar .address{right:110px;top:11px;display:flex;align-items:center;gap:8px}

/* header */
.brand{display:flex;align-items:center;gap:10px;font-family:"Montserrat",sans-serif;font-weight:600;color:var(--pink);font-size:17px;line-height:1.15}
.brand i{display:block;width:34px;height:34px;border-radius:50%;background:var(--pink-soft);flex:none}
.header .brand{left:137px;top:82px}
.contact-chip{display:flex;align-items:center;gap:8px;font-family:"Montserrat",sans-serif;font-size:11px;color:var(--ink)}
.contact-chip small{display:block;font-size:9px;font-weight:600}
.chip-ico{width:24px;height:24px;border-radius:50%;background:var(--pink);display:flex;align-items:center;justify-content:center}
.nav{left:500px;top:128px;display:flex;gap:37px;font-family:"Montserrat",sans-serif;font-size:12px;font-weight:500;color:var(--ink)}
.nav .active{color:var(--pink);border-bottom:2px solid var(--pink);padding-bottom:8px}

/* hero */
.hero-photo{left:0;top:174px;width:1200px;height:692px;background:linear-gradient(100deg,#e9e4e6 0%,#f4f1f2 40%,#c9d6e6 70%,#eef0f4 100%)}
.hero-card{left:314px;top:306px;width:611px;height:362px;background:rgba(229,70,152,.78);border-radius:8px;text-align:center;color:var(--white);padding-top:48px}
.hero-card h1{font-size:37px;line-height:52px;font-weight:500}
.hero-card p{font-size:14px;line-height:27px;margin:12px auto 0;width:470px}
.hero-card .btn{margin-top:16px;width:230px;height:46px;line-height:46px;font-size:13px}
.side-social{left:1100px;top:274px;display:flex;flex-direction:column;gap:16px;align-items:center}
.side-social span{width:18px;height:18px;border-radius:3px;border:1.5px solid var(--pink);display:block}
.side-social .boxed{width:38px;height:34px}
.scroll-line{left:1118px;top:438px;width:2px;height:82px;background:var(--pink)}
.scroll-text{left:1068px;top:570px;transform:rotate(-90deg);font-family:"Montserrat",sans-serif;font-size:11px;font-weight:600;color:var(--pink);letter-spacing:2px}

/* services */
.service{top:790px;width:241px;height:261px;background:var(--white);box-shadow:0 4px 14px rgba(0,0,0,.08);text-align:center;padding-top:58px}
.service .badge{position:absolute;left:73px;top:-47px;width:94px;height:94px;border-radius:50%;background:var(--pink);display:flex;align-items:center;justify-content:center}
.service h3{font-size:21px;color:var(--ink);font-weight:400}
.service p{font-size:12.5px;line-height:25px;color:var(--ink);margin:8px 16px 0;height:125px;overflow:hidden}

/* about */
.about-photo{left:0;top:1156px;width:617px;height:509px;background:linear-gradient(120deg,#dde6ee,#f3f3f3 50%,#cfd9e6)}
.about-panel{left:617px;top:1156px;width:583px;height:509px;background:var(--pink);color:var(--white);padding:50px 60px 0 61px}
.about-panel h2{font-size:42px;font-weight:600;margin-bottom:16px}
.about-panel p{font-size:14.5px;line-height:27px;margin-bottom:12px}
.about-panel .btn{width:173px;height:46px;line-height:46px;margin-top:8px}

/* accepting */
.accepting{left:0;top:1665px;width:1200px;height:640px;background:linear-gradient(90deg,#e6e4e5,#f1f0f0 30%,#f1f0f0 70%,#e4e2e3);text-align:center;padding-top:72px}
.accepting h2{font-size:38px;color:var(--ink)}
.rule{width:90px;height:3px;background:var(--pink);margin:14px auto 0}
.accepting h3{font-size:23px;color:var(--ink);margin:16px 0 12px}
.accepting p{font-size:14.3px;line-height:27px;width:740px;margin:0 auto 12px;color:var(--text)}
.accepting .btn{width:228px;height:43px;line-height:43px;margin-top:2px}

/* news */
.news-title{left:0;top:2378px;width:1200px;text-align:center}
.news-title h2{font-size:38px;color:var(--ink)}
.news-card{top:2468px;width:299px;height:377px;border:1px solid #d7d7d7;background:var(--white)}
.news-card .thumb{height:215px;position:relative}
.news-card .date{position:absolute;left:0;bottom:0;background:var(--pink);color:var(--white);font-family:"Montserrat",sans-serif;font-size:11px;font-weight:600;padding:5px 16px;border-radius:0 10px 0 0}
.news-card h4{font-size:13.5px;font-weight:700;line-height:15px;color:var(--ink);margin:22px 26px 8px;text-transform:uppercase}
.news-card p{font-size:11px;line-height:15px;margin:0 26px}
.news-card .btn{margin:14px 0 0 26px;width:118px;height:36px;line-height:32px;font-size:11px}

/* contact */
.contact-panel{left:0;top:2937px;width:601px;height:645px;background:var(--pink);padding:120px 0 0 103px}
.contact-panel h2{font-size:38px;color:var(--white);font-weight:500;margin-bottom:16px}
.field{background:var(--white);border:1px solid var(--pink-soft);font-family:"Montserrat",sans-serif;font-size:15px;color:#aaa;padding:12px 15px;height:45px}
.row{display:flex;gap:6px;margin-bottom:14px}
.row .field{width:212px}
.field.msg{width:432px;height:134px}
.contact-panel .btn{margin-top:16px;width:133px;height:39px;line-height:35px;border:2px solid var(--white);color:var(--white);font-size:12px}
.contact-photo{left:601px;top:2937px;width:599px;height:645px;background:linear-gradient(90deg,#c9d3dc,#eef0f2 40%,#f5f5f5 70%,#c6cfd8)}

/* footer */
.footer .brand{left:137px;top:3700px}
.footer .social-dots{position:absolute;left:132px;top:3796px;gap:14px}
.footer .social-dots span{width:31px;height:31px;background:var(--pink)}
.fcol{top:3682px;padding-left:14px;border-left:3px solid var(--pink)}
.fcol h4{font-size:17px;font-weight:600;color:var(--ink);margin-bottom:14px}
.fcol ul{list-style:none;font-family:"Montserrat",sans-serif;font-size:13px;color:#555}
.fcol li{margin-bottom:13px}
.fcol.small h4{font-size:13px}
.info-row{display:flex;align-items:center;gap:12px;margin-bottom:12px;font-family:"Montserrat",sans-serif;font-size:11px;color:#666;line-height:13px}
.info-row .chip-ico{width:31px;height:31px;flex:none}
.copyright{left:0;top:3939px;width:1200px;height:64px;background:var(--pink-mist);text-align:center;line-height:64px;font-size:10px;color:#666;border-top:1px solid var(--pink-pale)}
</style>
</head>
<body>

<!-- top bar -->
<div class="abs topbar">
  <span class="abs follow">FOLLOW US</span>
  <div class="social-dots"><span></span><span></span><span></span><span></span></div>
  <div class="abs address">
    <svg width="11" height="14" viewBox="0 0 12 16"><path d="M6 0a6 6 0 0 0-6 6c0 4.5 6 10 6 10s6-5.5 6-10a6 6 0 0 0-6-6zm0 8.5A2.5 2.5 0 1 1 6 3.5a2.5 2.5 0 0 1 0 5z" fill="#fff"/></svg>
    1840 WILLOWBROOK AVENUE, SUITE 210, ALDEN, CA 90210
  </div>
</div>

<!-- header -->
<header class="header">
  <div class="abs brand"><i></i><span>Larkfield<br>Women's Care</span></div>
  <div class="abs contact-chip" style="left:750px;top:72px">
    <span class="chip-ico"><svg width="12" height="9" viewBox="0 0 12 9"><rect x=".5" y=".5" width="11" height="8" fill="none" stroke="#fff"/><path d="M.5.5 6 5l5.5-4.5" fill="none" stroke="#fff"/></svg></span>
    <div><small>EMAIL US</small>admin@larkfieldwomenscare.com</div>
  </div>
  <div class="abs contact-chip" style="left:954px;top:72px">
    <span class="chip-ico"><svg width="11" height="11" viewBox="0 0 24 24"><path d="M6.6 10.8a15 15 0 0 0 6.6 6.6l2.2-2.2a1 1 0 0 1 1-.25 11 11 0 0 0 3.6.6 1 1 0 0 1 1 1V20a1 1 0 0 1-1 1A17 17 0 0 1 3 4a1 1 0 0 1 1-1h3.5a1 1 0 0 1 1 1 11 11 0 0 0 .6 3.6 1 1 0 0 1-.25 1z" fill="#fff"/></svg></span>
    <div><small>CALL US NOW</small>555-014-7783</div>
  </div>
  <nav class="abs nav">
    <span class="active">HOME</span><span>ABOUT US</span><span>OUR SERVICES</span><span>NEWS</span><span>RECOURSES</span><span>CONTACT US</span>
  </nav>
</header>

<!-- hero -->
<section>
  <div class="abs hero-photo" role="img" aria-label="Photo of a pregnant patient lying down while a smiling doctor listens with a stethoscope"></div>
  <div class="abs hero-card">
    <h1>WELCOME TO LARKFIELD<br>WOMEN'S CARE, ALDEN, CA</h1>
    <p>At Larkfield Women's Care in Alden, California, we believe better health starts when the patient is educated. For this reason, we take time to listen to our patients concerns, explain.</p>
    <span class="btn btn-white">BOOK AN APPOINTMENT</span>
  </div>
  <div class="abs side-social"><span class="boxed"></span><span></span><span></span></div>
  <div class="abs scroll-line"></div>
  <div class="abs scroll-text">SCROLL DOWN ›</div>
</section>

<!-- services -->
<section>
  <div class="abs service" style="left:96px">
    <span class="badge"><svg width="40" height="44" viewBox="0 0 40 44" fill="none" stroke="#fff" stroke-width="2"><circle cx="20" cy="8" r="5"/><path d="M15 18c-3 6-2 14 3 22M24 16c6 4 7 12 1 16"/></svg></span>
    <h3>Preganancy Care</h3>
    <p>Receiving regular care in pregnancy is important for the health of both you and your baby. Our obstetricians work with you every step of the way during your</p>
  </div>
  <div class="abs service" style="left:353px">
    <span class="badge"><svg width="40" height="40" viewBox="0 0 40 40" fill="none" stroke="#fff" stroke-width="2"><rect x="7" y="8" width="20" height="26" rx="2"/><path d="M12 16h10M12 22h10"/><circle cx="29" cy="29" r="6"/></svg></span>
    <h3>Birth Control</h3>
    <p>Our gynecologists are knowledgeable on all forms of birth control including the IUD, implants, vaginal rings, birth control pills, and more! We would</p>
  </div>
  <div class="abs service" style="left:611px">
    <span class="badge"><svg width="40" height="40" viewBox="0 0 40 40" fill="none" stroke="#fff" stroke-width="2"><rect x="5" y="7" width="30" height="20" rx="2"/><path d="M14 33h12M20 27v6M10 17h5l3-5 4 9 3-4h5"/></svg></span>
    <h3>Well Woman Exams</h3>
    <p>Our providers will help you to stay healthy by performing a physical exam on you annually. We will screen you for multiple health conditions that may pose a risk to</p>
  </div>
  <div class="abs service" style="left:869px">
    <span class="badge"><svg width="40" height="44" viewBox="0 0 40 44" fill="none" stroke="#fff" stroke-width="2"><circle cx="20" cy="12" r="7"/><path d="M8 40c0-10 5-16 12-16s12 6 12 16M17 28v6M23 28v6"/></svg></span>
    <h3>Women's Health</h3>
    <p>Whether you are dealing with painful or irregular periods, fibroids, or other women's health issues, we can help. We offer a variety of the most up-to-date</p>
  </div>
</section>

<!-- about -->
<section>
  <div class="abs about-photo" role="img" aria-label="Photo of a smiling pregnant woman with a doctor taking notes beside her"></div>
  <div class="abs about-panel">
    <h2>ABOUT US</h2>
    <p>Larkfield Women's Care in Alden, California, was formed in October of 2005 by Dr. Martin Hale.</p>
    <p>And Dr. Clara Venn. to help service the greats need for women's health services in West Alden County. In October of 2012, Dr. Hale retired, and Dr. Rosa Whitley joined the practice. In December of 2015, Dr. Whitley left the practice, leaving Dr. Venn to carry on as a solo practitioner. In November of 2022, Dr. Leila Farouk joined the Larkfield Women's Care family.</p>
    <span class="btn btn-white">EXPLORE MORE</span>
  </div>
</section>

<!-- accepting -->
<section class="abs accepting">
  <h2>NOW ACCEPTING NEW PATIENTS</h2>
  <div class="rule"></div>
  <h3>YOUR OB/GYN SPECIALISTS</h3>
  <p>Larkfield Women's Care offers you the best care possible in a personalized setting. We are currently accepting patients. Call our office now to make an appointment.</p>
  <p>Larkfield Women's Care (located near Alden Valley Hospital in Alden, CA) is a medical office that specializes in Christ-centered healthcare for women of all ages. Our team of exclusively female providers have years of experience taking care of women with a variety of pregnancy and gynecology concerns.</p>
  <p>Whether you need a routine examination, help during your pregnancy, have questions on birth control, or another female concern, we offer the best care possible for our patients. That is why better health starts here.</p>
  <p>Our office provides you with an environment where you can feel comfortable and where you know you will be in good hands. Our providers are leaders women's health. Dr. Venn is a board certified obstetrician and gynecologist. Dr. Farouk is a board eligible obstetrician and gynecologist.</p>
  <span class="btn btn-pink">BOOK AN APPOINTMENT</span>
</section>

<!-- news -->
<section>
  <div class="abs news-title"><h2>OBGYN NEWS</h2><div class="rule"></div></div>
  <article class="abs news-card" style="left:138px">
    <div class="thumb" role="img" aria-label="Photo of a pregnant patient at an ultrasound appointment" style="background:linear-gradient(120deg,#d9d4d0,#f2efec 55%,#b9aca4)"><span class="date">DEC 15, 2021</span></div>
    <h4>Lorem ipsum dolor sit amet consectetur adipiscing</h4>
    <p>Duis aute irure dolor in reprehenderit in voluptate velit esse cillum dolore</p>
    <span class="btn btn-outline">LEARN MORE</span>
  </article>
  <article class="abs news-card" style="left:452px">
    <div class="thumb" role="img" aria-label="Photo of a woman resting on white bedding" style="background:linear-gradient(120deg,#cfc9c4,#f1ede9 45%,#a07a5e)"><span class="date">DEC 15, 2021</span></div>
    <h4>When is the most appropriate time to have sex in order to get pregnant?</h4>
    <p>Duis aute irure dolor in reprehenderit in voluptate velit esse cillum dolore</p>
    <span class="btn btn-outline">LEARN MORE</span>
  </article>
  <article class="abs news-card" style="left:772px">
    <div class="thumb" role="img" aria-label="Photo of a couple looking at a pregnancy test together" style="background:linear-gradient(120deg,#e7e3e0,#f7f5f3 50%,#9fa9b8)"><span class="date">DEC 15, 2021</span></div>
    <h4>Lorem ipsum dolor sit amet consectetur adipiscing</h4>
    <p>Duis aute irure dolor in reprehenderit in voluptate velit esse cillum dolore</p>
    <span class="btn btn-outline">LEARN MORE</span>
  </article>
</section>

<!-- contact -->
<section>
  <div class="abs contact-panel">
    <h2>CONTACT US</h2>
    <div class="row"><div class="field">First name</div><div class="field">Last name</div></div>
    <div class="row"><div class="field">Email Address</div><div class="field">Phone</div></div>
    <div class="field msg">Message</div>
    <span class="btn">SUBMIT NOW</span>
  </div>
  <div class="abs contact-photo" role="img" aria-label="Photo of a smiling female doctor holding a stethoscope in a bright clinic hallway"></div>
</section>

<!-- footer -->
<footer class="footer">
  <div class="abs brand"><i></i><span>Larkfield<br>Women's Care</span></div>
  <div class="social-dots"><span></span><span></span><span></span><span></span></div>
  <div class="abs fcol" style="left:401px;top:3682px">
    <h4>Navigation</h4>
    <ul style="padding-left:8px"><li>Home</li><li>About us</li><li>News</li><li>Our Services</li><li>Patient Recourses</li><li>Contact us</li></ul>
  </div>
  <div class="abs fcol small" style="left:642px">
    <h4>Other Links</h4>
    <ul><li>Terms &amp; Conditions</li><li>Privacy Policy</li></ul>
  </div>
  <div class="abs fcol small" style="left:847px">
    <h4>Contact Information</h4>
    <div class="info-row"><span class="chip-ico"><svg width="12" height="16" viewBox="0 0 12 16"><path d="M6 0a6 6 0 0 0-6 6c0 4.5 6 10 6 10s6-5.5 6-10a6 6 0 0 0-6-6zm0 8.5A2.5 2.5 0 1 1 6 3.5a2.5 2.5 0 0 1 0 5z" fill="#fff"/></svg></span><span>1840 Willowbrook Avenue, Suite<br>210, Alden, CA 90210</span></div>
    <div class="info-row"><span class="chip-ico"><svg width="13" height="13" viewBox="0 0 24 24"><path d="M6.6 10.8a15 15 0 0 0 6.6 6.6l2.2-2.2a1 1 0 0 1 1-.25 11 11 0 0 0 3.6.6 1 1 0 0 1 1 1V20a1 1 0 0 1-1 1A17 17 0 0 1 3 4a1 1 0 0 1 1-1h3.5a1 1 0 0 1 1 1 11 11 0 0 0 .6 3.6 1 1 0 0 1-.25 1z" fill="#fff"/></svg></span><span>(555) 014-7066</span></div>
    <div class="info-row"><span class="chip-ico"><svg width="13" height="10" viewBox="0 0 12 9"><rect x=".5" y=".5" width="11" height="8" fill="none" stroke="#fff"/><path d="M.5.5 6 5l5.5-4.5" fill="none" stroke="#fff"/></svg></span><span>admin@larkfieldwomenscare.com</span></div>
  </div>
  <div class="abs copyright">© 2022 larkfieldwomenscare All Right Reserved</div>
</footer>

</body>
</html>
```